Luxury WordPress Website for CORALBASINS

I need a professional WordPress website for Coral Basins. The site should be modern, visually appealing, and user-friendly, reflecting the brand’s luxury and premium identity. It must include a homepage, product/service pages, contact form, and be responsive on both desktop and mobile devices. The design should allow for easy updates and integration of future content, while maintaining a polished and professional look.

Target Market(s)

swimmingpool & spa

Industry/Entity Type

Swimmingpool

Coding

Coded - Design and coding required

Font styles to use
Other font styles liked:
• HaboroSoft

Requirements
Must have
• Exclusive appearance
Nice to have
• • A logo that subtly incorporates water or pool elements. • A color palette that reflects luxury, elegance, and relaxation. • Clean and modern typography that is easy to read across all media. • Iconography or design elements that convey premium quality. • A versatile design that can be adapted for social media, merchandise, and promotional materials. • Optional: A tagline that emphasizes luxury and high-end pool experiences.

```html
<!DOCTYPE html>
<html lang="en">
<head>
<meta charset="utf-8">
<title>Coral Basins — Luxury Pools</title>
<link href="https://fonts.googleapis.com/css2?family=Outfit:wght@300;400;500;600;700&display=swap" rel="stylesheet">
<style>
:root{
  --navy:#0a1a63;
  --navy-deep:#071450;
  --blue:#1e7ef0;
  --ink:#0b1a5e;
  --text:#4a5270;
  --white:#ffffff;
  --foot:#eef0f4;
  --mist:#f1f3f8;
}
*{margin:0;padding:0;box-sizing:border-box}
html,body{width:1200px;height:4454px;overflow:hidden;background:#fff}
body{position:relative;font-family:"Outfit",sans-serif;color:var(--ink)}
.abs{position:absolute}
a{color:inherit;text-decoration:none}

/* top bar */
.topbar{left:0;top:0;width:1200px;height:29px;background:var(--navy-deep)}
.topbar .links{left:124px;top:8px;font-size:10px;color:#fff;display:flex;gap:26px;font-weight:500}
.topbar .social{left:800px;top:0;width:400px;height:29px;background:var(--blue);display:flex;justify-content:flex-end;align-items:center;gap:22px;padding-right:124px}
.topbar .social span{width:9px;height:9px;background:#fff;border-radius:2px;display:block;opacity:.9}

/* header */
.logo{font-weight:600;color:var(--ink)}
.header-logo{left:123px;top:52px;font-size:29px;letter-spacing:-.5px}
.nav{left:407px;top:61px;display:flex;gap:24px;font-size:11px;font-weight:500;color:var(--ink)}
.nav .active{color:var(--blue)}
.call{left:942px;top:52px;display:flex;gap:10px;align-items:center}
.call .ico{width:28px;height:28px;border-radius:50%;background:var(--navy);display:flex;align-items:center;justify-content:center}
.call .lbl{font-size:10px;color:var(--text)}
.call .num{font-size:12.5px;font-weight:600}

/* hero */
.hero-img{left:524px;top:102px;width:676px;height:533px;background:linear-gradient(180deg,#8fc3e8 0%,#5e9a5a 38%,#2ea6e0 62%,#c9c4b8 100%);clip-path:polygon(0 0,100% 0,100% 100%,7% 100%,0 90%)}
.hero-title{left:123px;top:172px;font-size:55px;line-height:54px;font-weight:600;color:var(--ink);z-index:2;letter-spacing:-.5px}
.hero-band{left:0;top:394px;width:524px;height:178px;background:var(--blue)}
.hero-band p{left:124px;top:34px;width:330px;font-size:12px;line-height:16px;color:#fff;font-weight:300}
.btn{display:flex;align-items:center;justify-content:center;border-radius:20px;font-size:9.5px;font-weight:600;text-transform:uppercase;letter-spacing:.2px}
.btn-white{left:124px;top:99px;width:182px;height:37px;background:#fff;color:var(--ink)}
.btn-blue{background:var(--blue);color:#fff}

/* section labels */
.eyebrow{font-size:8.5px;font-weight:600;color:var(--blue);text-transform:uppercase;letter-spacing:.3px}
.h2{font-size:29px;font-weight:600;text-transform:uppercase;letter-spacing:-.3px}
.center{left:0;width:1200px;text-align:center}

/* about */
.about-main{left:150px;top:820px;width:288px;height:318px;clip-path:polygon(0 0,100% 0,100% 88%,88% 100%,0 100%);background:linear-gradient(180deg,#4a98e0 0%,#b69a6a 35%,#56a046 55%,#6fb7cf 80%,#3c86b8 100%)}
.about-text{left:486px;top:858px;width:310px;font-size:11.5px;line-height:16px;color:var(--text);font-weight:300}
.about-small-1{left:890px;top:726px;width:118px;height:116px;clip-path:polygon(0 0,85% 0,100% 15%,100% 100%,0 100%);background:linear-gradient(180deg,#3f7c3a 0%,#4a8d3c 50%,#2b9ae0 70%,#b8b3a5 100%)}
.about-small-2{left:674px;top:970px;width:115px;height:104px;clip-path:polygon(0 0,85% 0,100% 15%,100% 100%,0 100%);background:linear-gradient(180deg,#8cc6ee 0%,#3f7a38 45%,#29a3df 70%,#cfc8b9 100%)}
.about-tall{left:849px;top:873px;width:201px;height:282px;clip-path:polygon(0 0,100% 0,100% 100%,12% 100%,0 92%);background:linear-gradient(180deg,#9ccaf0 0%,#4f8a46 40%,#0e2e4a 62%,#5ea24b 85%,#6bad4e 100%)}

/* services */
.services{left:0;top:1243px;width:1200px;height:623px;background:radial-gradient(circle at 30% 20%,#1a2f8a 0%,var(--navy) 50%,var(--navy-deep) 100%)}
.card{top:183px;width:225px}
.card .img{width:225px;height:255px;clip-path:polygon(0 0,100% 0,100% 88%,88% 100%,0 100%)}
.card h3{margin-top:20px;font-size:14.5px;font-weight:600;color:#fff;text-transform:uppercase}
.card p{margin-top:7px;font-size:11px;line-height:15px;color:#c9d2f0;font-weight:300;width:205px}
.btn-services{left:520px;top:1847px;width:160px;height:36px}

/* video */
.mist{background:linear-gradient(180deg,rgba(241,243,248,0) 0%,var(--mist) 30%,var(--mist) 70%,rgba(241,243,248,0) 100%)}
.play{left:280px;top:2093px;width:70px;height:70px;border-radius:50%;background:var(--navy);display:flex;align-items:center;justify-content:center}

/* why */
.why-title{left:161px;top:2656px;font-size:30px;line-height:37px;font-weight:600;text-transform:uppercase;letter-spacing:-.4px}
.feat{top:2645px;width:104px;text-align:center}
.feat .box{width:104px;height:96px;clip-path:polygon(0 0,86% 0,100% 14%,100% 100%,0 100%);display:flex;align-items:center;justify-content:center}
.feat p{margin:16px 0 0 -6px;width:116px;font-size:8.5px;line-height:12px;font-weight:500;text-transform:uppercase}

/* gallery */
.gallery-band{left:0;top:2900px;width:934px;height:679px;background:radial-gradient(circle at 40% 30%,#142a85,var(--navy) 55%,var(--navy-deep))}
.gallery-img{left:124px;top:3052px;width:951px;height:430px;background:linear-gradient(180deg,#6fb0ea 0%,#a9d2f2 22%,#3a6b2e 45%,#2a9ee6 62%,#d8d8d2 78%,#c9c9c3 100%)}
.dots{left:61px;top:3187px;display:flex;flex-direction:column;gap:8px}
.dots span{width:2px;height:34px;background:#fff;display:block}
.dots span.on{background:var(--blue)}

/* cta */
.cta-p{top:3812px;font-size:11.5px;line-height:16px;color:var(--text);font-weight:300}
.pool{left:351px;top:3968px;width:498px;height:90px;clip-path:polygon(14% 0,86% 0,100% 100%,0 100%);background:linear-gradient(180deg,#8ee0f4 0%,#36b6e6 50%,#1675c9 100%)}

/* footer */
.footer{left:0;top:4058px;width:1200px;height:335px;background:var(--foot)}
.foot-logo{left:121px;top:4165px;font-size:45px;letter-spacing:-.5px}
.socials{left:173px;top:4238px;display:flex;gap:5px}
.socials span{width:38px;height:38px;border-radius:50%;border:1.5px solid var(--ink);display:flex;align-items:center;justify-content:center}
.socials i{width:12px;height:12px;background:var(--ink);border-radius:50%;display:block}
.fcol{top:4162px}
.fcol h4{font-size:12.5px;font-weight:600;text-transform:uppercase;margin-bottom:10px}
.fcol li{list-style:none;font-size:9.5px;line-height:16.5px;color:var(--text)}
.contact-row{display:flex;gap:10px;font-size:9.5px;line-height:14px;color:var(--text);margin-bottom:14px}
.contact-row svg{flex:none;margin-top:2px}
.news p{font-size:9.5px;line-height:14px;color:var(--text);width:180px}
.news .input{margin-top:12px;width:184px;height:33px;border-radius:17px;background:#dde1ea;font-size:8.5px;color:#8a90a6;display:flex;align-items:center;padding-left:18px}
.news .btn{margin-top:9px;width:184px;height:32px}
.copy{left:0;top:4393px;width:1200px;height:61px;background:var(--navy-deep);color:#fff;font-size:9.5px;font-weight:500;display:flex;align-items:center;justify-content:center}
</style>
</head>
<body>

<div class="abs topbar">
  <div class="abs links"><a>Conditions</a><a>Quality</a><a>Stay Connected</a></div>
  <div class="abs social"><span></span><span></span><span></span><span></span><span></span></div>
</div>

<div class="abs logo header-logo">Coral Basins</div>
<nav class="abs nav">
  <a class="active">Home</a><a>Features ⌄</a><a>About Us ⌄</a><a>Services ⌄</a><a>Blog ⌄</a><a>Contacts</a>
</nav>
<div class="abs call">
  <div class="ico"><svg width="13" height="13" viewBox="0 0 24 24"><path fill="#fff" d="M6.6 10.8a15 15 0 0 0 6.6 6.6l2.2-2.2a1 1 0 0 1 1-.25 11.4 11.4 0 0 0 3.6.57 1 1 0 0 1 1 1V20a1 1 0 0 1-1 1A17 17 0 0 1 3 4a1 1 0 0 1 1-1h3.5a1 1 0 0 1 1 1c0 1.25.2 2.45.57 3.57a1 1 0 0 1-.25 1z"/></svg></div>
  <div><div class="lbl">Call us</div><div class="num">+00 555 010 247</div></div>
</div>

<div class="abs hero-img" role="img" aria-label="Large villa with a bright blue rectangular pool and lawn under trees"></div>
<h1 class="abs hero-title">EXPERIENCE<br>LUXURY, DIVE<br>INTO PERFECTION</h1>
<div class="abs hero-band">
  <p class="abs">At Coral Basins, we specialize in designing and<br>building luxury swimming pools that combine aesthetic<br>beauty with exceptional functionality.</p>
  <a class="abs btn btn-white">Get your free consultation</a>
</div>

<div class="abs eyebrow" style="left:150px;top:738px">About Coral Basins</div>
<h2 class="abs h2" style="left:150px;top:753px">Crafting premium pool experiences</h2>
<div class="abs about-main" role="img" aria-label="Round spa pool beside a villa terrace with palm trees"></div>
<p class="abs about-text">At Coral Basins, we specialize in designing and building luxury swimming pools that combine aesthetic beauty with exceptional functionality. From modern infinity pools to timeless classic designs, we create outdoor sanctuaries tailored to your lifestyle.</p>
<a class="abs btn btn-blue" style="left:486px;top:961px;width:116px;height:37px">Find out more</a>
<div class="abs about-small-1" role="img" aria-label="Garden pool framed by hedges"></div>
<div class="abs about-small-2" role="img" aria-label="Freeform pool in a green backyard"></div>
<div class="abs about-tall" role="img" aria-label="Infinity pool by the sea with palm trees"></div>

<section class="abs services">
  <div class="abs eyebrow center" style="top:100px">Our services</div>
  <h2 class="abs h2 center" style="top:118px;color:#fff">Bespoke pool solutions for every vision</h2>
  <div class="abs card" style="left:124px">
    <div class="img" role="img" aria-label="Custom pool beside a Mediterranean-style home" style="background:linear-gradient(180deg,#8fc4ee,#c7a48b 35%,#38b2e0 65%,#6aa858)"></div>
    <h3>Custom pool design</h3><p>Personalized designs that reflect your taste and outdoor space.</p>
  </div>
  <div class="abs card" style="left:367px">
    <div class="img" role="img" aria-label="Builder reviewing pool plans on site" style="background:linear-gradient(180deg,#e8dcc0,#8a9a6a 40%,#5a7fa8 70%,#2e9bd6)"></div>
    <h3>Pool design &amp; build</h3><p>Precision engineering for flawless results.</p>
  </div>
  <div class="abs card" style="left:607px">
    <div class="img" role="img" aria-label="Pool cleaning brush and hose above clear water" style="background:linear-gradient(180deg,#7fc6ee,#2a8fd6 50%,#1a5fb0)"></div>
    <h3>Maintenance &amp; upgrades</h3><p>Keep your pool pristine with expert care.</p>
  </div>
  <div class="abs card" style="left:849px">
    <div class="img" role="img" aria-label="Evening pool deck with warm lighting and loungers" style="background:linear-gradient(180deg,#0e1a1a,#3a3a2a 40%,#4ab6d0 60%,#8a5a32)"></div>
    <h3>Luxury accessories</h3><p>Lighting, heating, and water features to elevate your experience.</p>
  </div>
</section>
<a class="abs btn btn-blue btn-services">Discover our services</a>

<div class="abs eyebrow center" style="top:1975px">Watch our video</div>
<h2 class="abs h2 center" style="top:1990px">Build your dream swimming pool</h2>
<div class="abs mist" style="left:906px;top:2054px;width:294px;height:280px" role="img" aria-label="Soft wave decoration area"></div>
<div class="abs" style="left:180px;top:2187px;width:48px;height:228px;background:linear-gradient(180deg,#3f6a32,#7a7060)" role="img" aria-label="Pool garden detail"></div>
<div class="abs" style="left:235px;top:2210px;width:161px;height:283px;background:linear-gradient(180deg,#4a7a3a,#8a8478 45%,#2aa0d8)" role="img" aria-label="Rock waterfall and diving board at pool edge"></div>
<div class="abs" style="left:403px;top:2068px;width:221px;height:474px;background:linear-gradient(180deg,#9ccbee,#c8ccd2 30%,#6a8a5a 50%,#1f9ad8 75%,#8a8270)" role="img" aria-label="Large house behind a freeform pool with stone edging"></div>
<div class="abs" style="left:629px;top:2127px;width:277px;height:384px;background:linear-gradient(180deg,#a8d0f0,#d8dade 35%,#1f9ad8 70%,#a49e90)" role="img" aria-label="White villa with balcony overlooking a blue pool"></div>
<div class="abs" style="left:913px;top:2179px;width:107px;height:259px;background:linear-gradient(180deg,#2f5a2a,#5a7a48 60%,#8a8a7a)" role="img" aria-label="Trees and planters beside the pool"></div>
<div class="abs play"><svg width="12" height="12" viewBox="0 0 12 12"><path d="M3 1l8 5-8 5z" fill="#fff"/></svg></div>

<div class="abs eyebrow" style="left:162px;top:2642px">Why choose us</div>
<h2 class="abs why-title">Unmatched quality.<br>Exceptional<br>craftsmanship.</h2>
<div class="abs feat" style="left:550px">
  <div class="box" style="background:var(--blue)"><svg width="46" height="46" viewBox="0 0 46 46" fill="none" stroke="#fff" stroke-width="2"><circle cx="15" cy="14" r="6"/><circle cx="31" cy="14" r="6"/><path d="M4 40v-8a11 11 0 0 1 22 0v8M20 40v-8a11 11 0 0 1 22 0v8"/></svg></div>
  <p>Expert designers and builders with years of experience.</p>
</div>
<div class="abs feat" style="left:678px">
  <div class="box" style="background:var(--navy)"><svg width="46" height="46" viewBox="0 0 46 46" fill="none" stroke="#fff" stroke-width="2"><rect x="6" y="6" width="28" height="34" rx="2"/><path d="M12 14h16M12 20h16M12 26h10"/><circle cx="32" cy="32" r="6"/><path d="M36 36l5 5"/></svg></div>
  <p>Attention to<br>detail in every<br>project.</p>
</div>
<div class="abs feat" style="left:804px">
  <div class="box" style="background:var(--blue)"><svg width="46" height="46" viewBox="0 0 46 46" fill="none" stroke="#fff" stroke-width="2"><circle cx="23" cy="23" r="17" stroke-dasharray="3 3"/><path d="M15 31l16-16M15 15l16 16"/></svg></div>
  <p>Materials &amp; finishes that ensure durability &amp; elegance.</p>
</div>
<div class="abs feat" style="left:932px">
  <div class="box" style="background:var(--blue)"><svg width="46" height="46" viewBox="0 0 46 46" fill="none" stroke="#fff" stroke-width="2"><path d="M8 28h30M10 28l3 10h20l3-10M16 28V12h14v16M16 18h14M16 23h14"/><path d="M6 42c4-3 8 3 12 0s8 3 12 0 8 3 12 0"/></svg></div>
  <p>A seamless, stress free pool-building experience.</p>
</div>

<div class="abs gallery-band"></div>
<div class="abs eyebrow center" style="top:2965px">Our gallery</div>
<h2 class="abs h2 center" style="top:2982px;color:#fff">Pools that inspire</h2>
<div class="abs gallery-img" role="img" aria-label="Hillside pool terrace with loungers, stone wall and forest view"></div>
<div class="abs dots"><span></span><span></span><span class="on"></span><span></span></div>
<svg class="abs" style="left:1120px;top:3244px" width="34" height="44" viewBox="0 0 34 44" fill="none" stroke="#0b1a5e" stroke-width="1.6"><path d="M2 10h30M9 3L2 10l7 7M2 34h30M25 27l7 7-7 7"/></svg>

<div class="abs mist" style="left:0;top:3660px;width:187px;height:273px" role="img" aria-label="Soft wave decoration area"></div>
<div class="abs eyebrow center" style="top:3747px">Book consultation</div>
<h2 class="abs h2 center" style="top:3762px">Start your luxury pool journey today</h2>
<p class="abs center cta-p">Our team is ready to bring your dream pool to life. Schedule a consultation and<br>take the first step towards a premium pool experience.</p>
<a class="abs btn btn-blue" style="left:524px;top:3863px;width:152px;height:36px">Book a consultation</a>
<div class="abs pool" role="img" aria-label="Tiled swimming pool seen in perspective"></div>

<footer class="abs footer"></footer>
<div class="abs logo foot-logo">Coral Basins</div>
<div class="abs socials"><span><i></i></span><span><i></i></span><span><i></i></span><span><i></i></span></div>
<div class="abs fcol" style="left:451px"><h4>Company</h4><ul><li>Home</li><li>Features</li><li>About Us</li><li>Services</li><li>Blog</li><li>Contacts</li></ul></div>
<div class="abs fcol" style="left:585px"><h4>Customer</h4><ul><li>FAQ</li><li>Shipping</li><li>Login</li><li>Register</li><li>Terms of Service</li><li>Rewards</li></ul></div>
<div class="abs fcol" style="left:721px"><h4>Contact us</h4>
  <div class="contact-row"><svg width="10" height="10" viewBox="0 0 24 24"><path fill="#0b1a5e" d="M6.6 10.8a15 15 0 0 0 6.6 6.6l2.2-2.2a1 1 0 0 1 1-.25 11.4 11.4 0 0 0 3.6.57 1 1 0 0 1 1 1V20a1 1 0 0 1-1 1A17 17 0 0 1 3 4a1 1 0 0 1 1-1h3.5a1 1 0 0 1 1 1c0 1.25.2 2.45.57 3.57a1 1 0 0 1-.25 1z"/></svg><div>Phone:<br>555-010-248</div></div>
  <div class="contact-row"><svg width="10" height="10" viewBox="0 0 10 10"><circle cx="5" cy="5" r="4.5" fill="#0b1a5e"/><path d="M5 2.5V5h2" stroke="#fff" fill="none"/></svg><div>Hours:<br>Mon–Fri 8am – 6pm EST</div></div>
  <div class="contact-row"><svg width="10" height="10" viewBox="0 0 10 8"><rect width="10" height="8" rx="1" fill="#0b1a5e"/><path d="M0 1l5 3 5-3" stroke="#fff" fill="none"/></svg><div>Email:<br>hello@coralbasins.test</div></div>
</div>
<div class="abs fcol news" style="left:890px"><h4>Signup newsletter</h4>
  <p>Sign up to get the latest on sales, new releases and more ...</p>
  <div class="input">Enter email address</div>
  <a class="btn btn-blue">Signup</a>
</div>
<div class="abs copy">© COPYRIGHT 2025 CORAL BASINS ALL RIGHTS RESERVED</div>

</body>
</html>
```